KWB needs a professional PP

We are looking for a more professional powerpoint presentation that will be presented to prospective clients. This powerpoint needs to summarize all the services and value that The Harbinger Collective has to offer, pretty much giving an overview of the company.

The clients we deal with are Funeral Homes and Funeral Directors, we are an organization dedicated to assisting funeral homes in implementing highly profitable insurance programs while providing the training, support and service along the way. More information is provided in the brochure attached.

We are going for a professional simple theme, we want to get the message across without overwhelming the client.

I have attached our current powerpoint presentation as reference and more information about the our company and what we offer. This one is obviously what we are looking to replace, but the information will be generally the same. It needs to be more visually appealing and convey professionalism.

```html
<!DOCTYPE html>
<html lang="en">
<head>
<meta charset="UTF-8">
<title>The Harbinger Collective – Company Overview</title>
<link href="https://fonts.googleapis.com/css2?family=Cinzel:wght@400;700&family=Open+Sans:wght@700&family=Carlito:wght@400;700&display=swap" rel="stylesheet">
<style>
  :root {
    --brand-blue: #2f6aad;
    --title-blue: #2a5ea3;
    --body-grey: #6b6b6b;
    --cell-grey: #e9e7e8;
    --cell-text: #555555;
    --white: #ffffff;
  }
  * { margin: 0; padding: 0; box-sizing: border-box; }
  html, body { width: 1200px; height: 900px; overflow: hidden; background: var(--white); }
  .slide { position: relative; width: 1200px; height: 900px; background: var(--white); }

  .slide-header {
    position: absolute; left: 0; top: 0; width: 1200px; height: 117px;
    background: linear-gradient(to bottom, #f2f2f2 0%, #ffffff 60%, #fafafa 100%);
    box-shadow: 0 2px 6px rgba(0,0,0,0.08);
  }
  .project-title {
    position: absolute; left: 48px; top: 34px;
    font-family: "Cinzel", serif; font-weight: 700; font-size: 31px;
    color: var(--title-blue); letter-spacing: 0.5px;
  }
  .brand-name {
    position: absolute; right: 28px; top: 36px;
    font-family: "Cinzel", serif; font-weight: 700; font-size: 26px;
    color: var(--title-blue);
  }

  .content-title {
    position: absolute; left: 93px; top: 206px;
    font-family: "Cinzel", serif; font-weight: 700; font-size: 29px;
    color: var(--title-blue);
  }
  .content-body {
    position: absolute; left: 93px; top: 250px; width: 985px;
    font-family: "Cinzel", serif; font-weight: 400; font-size: 19px;
    line-height: 30px; color: var(--body-grey);
  }

  .info-table {
    position: absolute; left: 85px; top: 427px; width: 1030px;
    border-collapse: separate; border-spacing: 3px;
    background: var(--white);
    box-shadow: 0 0 6px rgba(0,0,0,0.18);
    table-layout: fixed;
  }
  .info-table th {
    height: 66px; background: var(--brand-blue); color: var(--white);
    font-family: "Open Sans", sans-serif; font-weight: 700; font-size: 23px;
    text-align: left; padding-left: 20px;
  }
  .info-table td {
    height: 66px; background: var(--cell-grey); color: var(--cell-text);
    font-family: "Carlito", sans-serif; font-size: 23px;
    padding-left: 18px;
  }

  .footer-rule {
    position: absolute; left: 0; top: 842px; width: 1200px; height: 2px;
    background: var(--brand-blue);
  }
  .slide-footer {
    position: absolute; left: 0; top: 849px; width: 1200px; height: 51px;
    background: var(--brand-blue); color: var(--white);
    font-family: "Carlito", sans-serif; font-size: 20px;
  }
  .copyright { position: absolute; left: 20px; top: 13px; }
  .page-number { position: absolute; right: 16px; top: 13px; font-weight: 700; }
</style>
</head>
<body>
<div class="slide">
  <header class="slide-header">
    <div class="project-title">COMPANY OVERVIEW</div>
    <div class="brand-name">The Harbinger Collective</div>
  </header>

  <h1 class="content-title">Who We Are</h1>
  <p class="content-body">
    The Harbinger Collective is an organization dedicated to assisting funeral homes and funeral directors in implementing highly profitable insurance programs. We provide the training, support and service needed at every step, from program design and staff coaching to ongoing account care, so each firm can serve families well and grow with confidence.
  </p>

  <table class="info-table">
    <thead>
      <tr><th>Insurance Programs</th><th>Training</th><th>Support &amp; Service</th></tr>
    </thead>
    <tbody>
      <tr><td>Preneed Funding Plans</td><td>Staff Onboarding</td><td>Dedicated Account Team</td></tr>
      <tr><td>Final Expense Coverage</td><td>Sales Coaching</td><td>Claims Assistance</td></tr>
      <tr><td>Custom Program Design</td><td>Compliance Guidance</td><td>Ongoing Program Reviews</td></tr>
    </tbody>
  </table>

  <div class="footer-rule"></div>
  <footer class="slide-footer">
    <span class="copyright">© The Harbinger Collective</span>
    <span class="page-number">Page : 01</span>
  </footer>
</div>
</body>
</html>
```